Cleaning Bochure for Different Services

We need to create preferably an A4 brochure for cleaning services so we are able to give to our customers upon meeting them. check out our website for more info. It is www.brightvalecare.co.uk We need a page on;-Commercial Cleaning-Carpet Cleaning-Oven Cleaning with description and some imagery.

Target Market(s)

Commercial Cleaning Customers

Industry/Entity Type

Office Cleaning

Font styles to use
Sans Serif

Colors
33a6d7
aaaaaa

Requirements
Must have
• 4 pages each containing these services
• -Commercial Cleaning (most important)
• -Carpet Cleaning
• -Oven Cleaning
Nice to have
• Clean and smart looking design use some imagination and possibly go wild!
• Must be eye catching!

```html
<!DOCTYPE html>
<html lang="en">
<head>
<meta charset="utf-8">
<title>Commercial Carpet Cleaning &amp; Oven Cleaning</title>
<link href="https://fonts.googleapis.com/css2?family=Montserrat:wght@300;400;500;700;800&display=swap" rel="stylesheet">
<style>
  :root {
    --brand-blue: #27a8d8;
    --panel-grey: #e8e8ea;
    --quote-grey: #9b9da0;
    --ink: #1d1d1f;
    --ink-soft: #333336;
    --white: #ffffff;
  }
  * { margin: 0; padding: 0; box-sizing: border-box; }
  html, body { width: 848px; height: 1200px; overflow: hidden; background: var(--white); }
  .page {
    position: relative; width: 848px; height: 1200px; overflow: hidden;
    font-family: 'Montserrat', sans-serif; color: var(--ink); background: var(--white);
  }
  .left-panel { position: absolute; left: 0; top: 0; width: 432px; height: 1200px; background: var(--panel-grey); }

  .title-band {
    position: absolute; left: 106px; top: 50px; width: 682px; height: 109px;
    background: var(--brand-blue); color: var(--white);
    text-align: right; padding: 6px 22px 0 0;
    font-weight: 700; font-size: 44px; line-height: 51px; letter-spacing: 0.5px;
  }

  .hero-photo {
    position: absolute; left: 0; top: 172px; width: 788px; height: 377px;
    background: linear-gradient(170deg, #8f7a60 0%, #b59a74 35%, #c9ad84 65%, #a58a66 100%);
  }
  .testimonial {
    position: absolute; left: 163px; top: 372px; width: 610px; height: 165px;
    background: var(--quote-grey); color: var(--white);
    padding: 6px 4px 0 5px;
    font-weight: 700; font-size: 20.5px; line-height: 25.7px;
  }
  .testimonial .author { font-weight: 500; }

  .service-heading { position: absolute; font-weight: 800; font-size: 22px; color: var(--brand-blue); letter-spacing: 0.3px; }
  .service-tag { position: absolute; font-weight: 500; font-size: 15px; line-height: 25.6px; letter-spacing: 0.6px; color: var(--ink); }
  .service-body { position: absolute; font-weight: 300; font-size: 17px; line-height: 25.6px; color: var(--ink-soft); letter-spacing: 0.5px; }

  .carpet-heading { left: 101px; top: 562px; }
  .carpet-tag { left: 101px; top: 597px; width: 320px; }
  .carpet-intro { left: 101px; top: 648px; width: 320px; }
  .stain-lead { position: absolute; left: 101px; top: 719px; width: 320px; font-weight: 500; font-size: 17px; line-height: 25.6px; letter-spacing: 0.3px; }
  .stain-list { position: absolute; left: 101px; top: 770px; list-style: none; font-weight: 300; font-size: 17px; line-height: 25.65px; letter-spacing: 0.6px; color: var(--ink-soft); }
  .stain-list li::before { content: "·"; margin-right: 6px; }

  .oven-heading { left: 477px; top: 562px; }
  .oven-tag { left: 477px; top: 597px; width: 300px; }
  .oven-intro { left: 477px; top: 648px; width: 310px; }

  .photo-frame { position: absolute; border: 5px solid var(--brand-blue); }
  .photo-fill { width: 100%; height: 100%; }
  .before-frame { left: 474px; top: 777px; width: 167px; height: 206px; }
  .before-frame .photo-fill { background: linear-gradient(180deg, #6c6d70 0%, #2d2d30 45%, #8a5a35 80%, #b9b4ad 100%); }
  .after-frame { left: 621px; top: 956px; width: 167px; height: 207px; }
  .after-frame .photo-fill { background: linear-gradient(180deg, #4f5256 0%, #26272a 55%, #7a6452 85%, #9a8470 100%); }

  .label-band {
    position: absolute; background: var(--brand-blue); color: var(--white);
    font-weight: 800; font-size: 21px; letter-spacing: 1px;
    display: flex; align-items: center; justify-content: center;
  }
  .before-label { left: 641px; top: 783px; width: 147px; height: 51px; padding-left: 8px; }
  .after-label { left: 474px; top: 1005px; width: 147px; height: 51px; }

  .price-note { position: absolute; left: 647px; top: 844px; width: 140px; font-weight: 300; font-size: 17px; line-height: 25.6px; letter-spacing: 0.5px; color: var(--ink-soft); }
</style>
</head>
<body>
<div class="page">
  <div class="left-panel"></div>

  <h1 class="title-band">Commercial Carpet Cleaning<br>&amp; Oven Cleaning</h1>

  <div class="hero-photo" role="img" aria-label="Freshly cleaned beige living room carpet with cleaning stripes in front of a sofa"></div>
  <blockquote class="testimonial">“I hired brightvale care as I spilt a bottle of red wine on my white/beige carpet and generally my carpet needed a good clean in my living room, the outcome was impressive! I felt as if we had a new carpet fitted! It looked brand new! No need to replace my carpet after all it was amazing.” <span class="author">- Dana Whitfield</span></blockquote>

  <h2 class="service-heading carpet-heading">Carpet Cleaning</h2>
  <p class="service-tag carpet-tag">LOCAL, FAMILY-RUN CARPET AND UPHOLSTERY CLEANING IN YORK</p>
  <p class="service-body carpet-intro">If you are looking for carpet cleaning, we’ve got you covered.</p>
  <p class="stain-lead">Our equipment can remove all marks and stains, including...</p>
  <ul class="stain-list">
    <li>Chewing gum</li><li>White wine</li><li>Red wine</li><li>Juice</li><li>Paint</li>
    <li>Crayon</li><li>Blue-tac</li><li>Playdough</li><li>Mould</li><li>Coffee</li>
    <li>Tea</li><li>Beer</li><li>Urine</li><li>Dust build-up</li><li>and more...</li>
  </ul>

  <h2 class="service-heading oven-heading">Oven Cleaning</h2>
  <p class="service-tag oven-tag">IN PARTNERSHIP WITH OVEN REVIVE.</p>
  <p class="service-body oven-intro">Tenants landlords and agents alike. Yorkshires leading oven cleaning and repair specialists.</p>

  <div class="photo-frame before-frame"><div class="photo-fill" role="img" aria-label="Range oven before cleaning with a greasy, stained door"></div></div>
  <div class="label-band before-label">BEFORE</div>
  <p class="price-note">Have your oven cleaned from as little as £45.00 (inc vat)</p>

  <div class="label-band after-label">AFTER</div>
  <div class="photo-frame after-frame"><div class="photo-fill" role="img" aria-label="Range oven after cleaning with a spotless open door"></div></div>
</div>
</body>
</html>
```